Winery needs MailChimp newsletter

Hi
We have a small vineyard in Australia and need a newsletter designed to send out whenever we release a new vintage or there's some special news - approx 4 times per year.
We would like the design [added: including colours etc] to be consistent with our website:
www.bertolvi.com.au
(let us know if you need info re colours, fonts etc)
Also see the label designs on our website under Wines / Pinot Gris and Wines / Pinot Noir, to get more of a look and feel for our brand.
We plan on using mailchimp to send the newsletter out (but let us know if you'd recommend a different approach). [added: we think we'll need the mailchimp coding/html]
We're uploading the logo, a photo of a misty morning that's been used on our marketing materials in the past, as well as a photo of the current vintage that this next newsletter will announce the release of [added: it's a photo of a wine barrel, please show the whole barrel, not just the top of the barrel]. If you see other images on the website you would like to incorporate etc, please let us know.
[added: we've also uploaded an image of the grey iron shed from the logo, to be used eg as a header/footer]
Please allow space for a short intro paragraph (approx. 25-50 words), and a second area for more detailed information (approx. 50-75 words), [added: and a third area for wrapping up/other info (approx. 25-50 words)]
Lastly, we need the newsletter to link to/incorporate a pdf order form which will also be uploaded.
Thank you for your interest in this project - please don't hesitate to let us know what questions you have, thanks!
Maren T.

```html
<!DOCTYPE html>
<html lang="en">
<head>
<meta charset="utf-8">
<title>Bertolvi – Newsletter</title>
<link rel="stylesheet" href="https://fonts.googleapis.com/css2?family=Arimo:ital@0;1&family=Gelasio:ital,wght@0,400;0,700;1,400&display=swap">
<style>
  :root {
    --navy: #22303f;
    --page: #ffffff;
    --ink: #111111;
    --body-text: #7d7468;
    --intro-text: #8a8070;
    --rule: #e3e0dc;
    --frame: #e8e5e1;
    --bar-text: #e6e8ea;
    --bar-link: #9aa5b0;
  }
  * { margin: 0; padding: 0; box-sizing: border-box; }
  html, body { width: 1200px; height: 2529px; overflow: hidden; background: var(--page); }
  body { position: relative; font-family: "Arimo", Arial, sans-serif; }

  .browser-bar {
    position: absolute; top: 0; left: 0; width: 1200px; height: 73px;
    background: var(--navy); color: var(--bar-text);
    font-family: "Gelasio", Georgia, serif; font-style: italic; font-size: 23px;
    display: flex; align-items: center; justify-content: center;
  }
  .browser-bar a { color: var(--bar-link); text-decoration: none; margin-left: 8px; }

  .hero {
    position: absolute; top: 73px; left: 0; width: 1200px; height: 441px;
    background:
      linear-gradient(to bottom, rgba(0,0,0,0) 70%, rgba(92,110,48,0.85) 88%, rgba(150,140,70,0.9) 98%, #d9c98a 100%),
      linear-gradient(to right, #2e3434 0%, #5d6261 25%, #8d918e 55%, #6f7471 80%, #3d4242 100%);
  }
  .brand-name {
    position: absolute; top: 205px; left: 0; width: 1200px; text-align: center;
    color: #ffffff; font-family: "Gelasio", Georgia, serif; font-weight: 400; font-size: 80px; line-height: 1;
  }

  .headline {
    position: absolute; top: 575px; left: 0; width: 1200px; text-align: center;
    font-family: "Gelasio", Georgia, serif; font-size: 66px; font-weight: 400; color: var(--ink);
  }
  .intro {
    position: absolute; top: 690px; left: 100px; width: 1000px; text-align: center;
    font-style: italic; font-size: 31px; line-height: 47px; color: var(--intro-text);
  }
  .lead {
    position: absolute; top: 858px; left: 32px; width: 1136px; text-align: center;
    font-size: 23.5px; line-height: 42px; color: var(--body-text);
  }
  .button {
    position: absolute; left: 360px; width: 483px; height: 73px;
    background: var(--navy); border-radius: 12px; color: #ffffff;
    font-family: "Gelasio", Georgia, serif; font-size: 29px; letter-spacing: 3px;
    display: flex; align-items: center; justify-content: center; text-decoration: none;
  }
  .button-find { top: 1141px; }
  .button-order { top: 1835px; }

  .section-title {
    position: absolute; left: 0; width: 1200px; text-align: center;
    font-family: "Gelasio", Georgia, serif; font-weight: 700; font-size: 29px; letter-spacing: 3px; color: var(--ink);
  }
  .section-rule { position: absolute; left: 56px; width: 1088px; height: 2px; background: var(--rule); }

  .vintage-photo {
    position: absolute; top: 1397px; left: 22px; width: 394px; height: 388px;
    background: var(--frame); padding: 16px;
  }
  .vintage-photo div {
    width: 100%; height: 100%;
    background: linear-gradient(160deg, #4a3a2c 0%, #8a6a4a 35%, #b08a62 55%, #6d4d34 80%, #3c2c20 100%);
  }
  .vintage-text {
    position: absolute; top: 1398px; left: 448px; width: 730px;
    font-size: 22px; line-height: 35px; color: var(--body-text);
  }
  .vintage-text p + p { margin-top: 35px; }

  .closing {
    position: absolute; top: 2090px; left: 50px; width: 1100px; text-align: center;
    font-size: 22px; line-height: 35px; color: var(--body-text);
  }

  .footer {
    position: absolute; top: 2332px; left: 0; width: 1200px; height: 197px; background: var(--navy);
    display: flex; align-items: center; justify-content: center; gap: 24px;
    color: #ffffff; font-family: "Gelasio", Georgia, serif; font-size: 28px;
  }
</style>
</head>
<body>
  <div class="browser-bar">Can't see this email? <a href="#">View it in your browser.</a></div>

  <div class="hero" role="img" aria-label="Misty morning over the vineyard with trees, fence posts and a grey iron shed"></div>
  <div class="brand-name">Bertolvi</div>

  <h1 class="headline">Bertolvi – our little 'shed'</h1>

  <p class="intro">Fusce lacinia id nisl ut ullamcorper. Nam feugiat consequat tortor non rhoncus. Donec in placerat nibh. Pellentesque habitant morbi tristique senectus et netus turpis egestas. Fusce ultrices consequat placerat.</p>

  <p class="lead">Vivamus dapibus arcu a ornare suscipit. Fusce non felis nisl. Quisque eu est lobortis erat gravida mattis et quis felis. Pellentesque habitant morbi tristique senectus et netus et malesuada fames ac turpis egestas. Aliquam erat volutpat. Cras cursus lectus eget nunc tempor feugiat. Curabitur id scelerisque elit. Praesent lacinia imperdiet nulla, a rhoncus est dignissim in. Vivamus dapibus arcu a ornare suscipit. Fusce non felis nisl. Quisque eu est lobortis erat gravida mattis et quis felis. Pellentesque habitant morbi tristique senectus et netus et malesuada fames ac turpis egestas.</p>

  <a class="button button-find" href="#">FIND OUT MORE</a>

  <h2 class="section-title" style="top:1290px;">DONEC EU ELEMENTUM NEQUE</h2>
  <div class="section-rule" style="top:1362px;"></div>

  <div class="vintage-photo"><div role="img" aria-label="Oak wine barrel of the new vintage with a glass resting on top"></div></div>
  <div class="vintage-text">
    <p>Pellentesque mattis auctor velit, at vehicula leo accumsan eget. Phasellus urna lectus, porttitor quis lacinia eu, fermentum ut odio. Duis faucibus turpis volutpat urna imperdiet pretium. Duis adipiscing lorem et pretium vestibulum. Duis massa enim, accumsan sed vulputate et, sodales et lorem. Sed non leo velit.</p>
    <p>Etiam auctor aliquam odio et feugiat. Proin hendrerit commodo feugiat. Etiam elit lectus, aliquet ut velit at, dapibus tincidunt libero. Duis pulvinar tincidunt libero non molestie. In magna dui, consectetur in elit vel, vehicula cursus mi. Morbi eu pellentesque quam, a gravida diam. Nam hendrerit, ipsum convallis vestibulum facilisis.</p>
  </div>

  <a class="button button-order" href="#">ORDER NOW</a>

  <h2 class="section-title" style="top:1987px;">MAECENAS LOREM SAPIEN, CURSUS</h2>
  <div class="section-rule" style="top:2054px;"></div>

  <p class="closing">Fusce lacinia at massa ut adipiscing. Integer non tortor sed mi aliquet tincidunt vel et ante. Donec quis est in risus sagittis viverra quis non elit. Fusce in dapibus tortor, at porttitor enim. Nam pretium dapibus lacinia. Pellentesque aliquet sed lacus sed malesuada. Nam adipiscing tellus in nunc porttitor feugiat. Maecenas et condimentum nisi. Sed non nisl sed nisl porta lobortis ac sed risus. Mauris sodales, justo vel ultrices porta, turpis nisi lobortis arcu, quis posuere lectus urna vitae diam.</p>

  <div class="footer">
    <svg width="58" height="58" viewBox="0 0 58 58" aria-hidden="true"><circle cx="29" cy="29" r="26" fill="none" stroke="#ffffff" stroke-width="3"/></svg>
    <span>FIND US ON CIRCLEBOOK</span>
  </div>
</body>
</html>
```